Your Harbor Agent Website Design

Creative Brief: Website Design for Your Harbor Agent
- Project Overview: Design a website for our new brand, "Your Harbor Agent". Your Harbor Agent is a service that matches clients with the perfect realtor. The primary function of this site is to serve as a lead generation hub, to generate leads of people who are looking to either buy or sell their house and need a great realtor. The site needs to have a very clean, modern design using sites like Tallyquest, Brickwell, Lantern, and Vexomill as an example. The site also needs to have a primary lead capture capability through a multi-step form or questionnaire that indicates if they are buying or selling, and depending on that selection, creates two different flows.

Target Audience:
- Homebuyers and sellers in the Denver area
- Individuals looking for high-quality realtor services
- Users seeking a seamless and professional online & home buying/selling experience

Objectives:
- Create a visually appealing, modern website with a strong emphasis on lead generation.
- Design advanced, multi-step forms for efficient lead capture.
- Ensure the website is user-friendly and optimized for both desktop and mobile devices.

Pages to Design:
Home Page:
- Engaging hero section with a clear call to action and the ability to enter the form flow
- Brief introduction to Your Harbor Agent and its unique value proposition
- Key features & benefits of being matched with a realtor by Your Harbor Agent
- Testimonials and success stories
- Lead capture form

About Page:
- Overview of Your Harbor Agent’s mission and values
- Professional and trust-building imagery

How it Works Page:
- Step-by-step explanation of the matching process (complete the form and we will match you with a realtor)
- Visual aids (icons, graphics) to simplify complex information
- Customer journey map from inquiry to successful match & sale of home
- Lead capture form

Contact Us Page:
- Simple and accessible contact form
- Contact details
- Call to action for immediate inquiries

Blog Template:
- Clean, easy-to-read layout for blog posts, primarily location/neighborhood guides as well as standard blogs
- Sidebar for recent posts, categories, and tags
- Social sharing buttons
- Lead capture form embedded within blog posts

Design Style:
- Modern and professional with a focus on usability
- Clean lines and intuitive navigation
- Use of curved corners and minimal straight lines for a sleek look
- Incorporation of graphic design elements, potentially including 3D and isomorphic design
- Inspired by sites like Tallyquest, Brickwell, Lantern, and Vexomill
Consistent color scheme and typography

Visual References:
- Tallyquest: For its professional and corporate look
- Brickwell and Lantern: For their user-friendly interfaces and modern design
- Vexomill: For its clean and functional layout

Target Market(s)

- Homebuyers and sellers in the Denver area, Individuals looking for high-quality realtor services, Users seeking a seamless and professional home buying/selling experience

Industry/Entity Type

Real Estate

Number of Pages Required

5+ page

Requirements
Must have
• Fully designed website with lead capture functionality based on brief
Nice to have
• Designed in Figma, Starting / Placeholder copy

```html
<!DOCTYPE html>
<html lang="en">
<head>
<meta charset="utf-8">
<title>Your Harbor Agent</title>
<link href="https://fonts.googleapis.com/css2?family=Poppins:wght@300;400;500;600&display=swap" rel="stylesheet">
<style>
:root{
  --navy:#2d3a7e;
  --orange:#ee7a35;
  --ink:#222;
  --muted:#555;
  --soft:#f8f7f8;
  --field:#ffffff;
  --line:#e4e4e8;
}
*{box-sizing:border-box;margin:0;padding:0}
html,body{width:1200px;height:5029px;overflow:hidden}
body{position:relative;font-family:'Poppins',sans-serif;color:var(--ink);background:#fff}
.abs{position:absolute}
.btn{position:absolute;display:flex;align-items:center;justify-content:center;font-size:17px;border-radius:3px}
.btn-fill{background:var(--orange);color:#fff}
.btn-line{border:1.5px solid var(--orange);color:var(--ink);background:#fff}
.tag{position:absolute;font-size:21px;font-weight:600;color:var(--navy);display:flex;align-items:center;gap:14px;letter-spacing:.3px;white-space:nowrap}
.tag i{display:block;width:42px;height:3px;background:var(--orange)}
.photo{position:absolute}

/* header */
.site-header{position:absolute;top:0;left:0;width:1200px;height:113px;background:#fff}
.brand{position:absolute;left:75px;top:46px;font-size:26px;font-weight:600;color:var(--navy);letter-spacing:.3px;white-space:nowrap}
.nav{position:absolute;top:52px;left:586px;display:flex;gap:27px;font-size:12.5px;color:#444;white-space:nowrap}
.nav .active{color:var(--navy);border-bottom:2px solid var(--orange);padding-bottom:4px}
.nav-cta{position:absolute;left:1015px;top:44px;width:109px;height:35px;background:var(--orange);color:#fff;font-size:12.5px;display:flex;align-items:center;justify-content:center;border-radius:3px}

/* hero */
.hero-title{left:75px;top:258px;font-size:42px;font-weight:500;line-height:55px;color:#222;white-space:nowrap}
.hero-text{left:75px;top:396px;width:520px;font-size:17px;line-height:27px;color:#333;white-space:nowrap}
.search-panel{left:75px;top:804px;width:1049px;height:146px;background:#eeedef}
.select{position:absolute;top:47px;width:199px;height:57px;background:#fff;border-radius:3px;font-size:14px;color:#333;padding:0 22px;display:flex;align-items:center;justify-content:space-between}
.select::after{content:"";border:6px solid transparent;border-top:8px solid #222;margin-top:8px}
.search-btn{position:absolute;top:47px;left:871px;width:152px;height:57px;background:var(--navy);color:#fff;border-radius:3px;font-size:14px;display:flex;align-items:center;justify-content:space-between;padding:0 26px}

/* about */
.about-title{left:600px;top:1258px;font-size:44px;font-weight:500;color:#222;white-space:nowrap}
.about-text{left:601px;top:1338px;width:520px;font-size:13px;line-height:22.5px;color:#555;white-space:nowrap}
.feature{position:absolute;display:flex;align-items:center;gap:16px;font-size:16px;line-height:19px;color:#222}
.feature-ring{width:76px;height:76px;border-radius:50%;background:#fff;box-shadow:0 2px 10px rgba(0,0,0,.12);display:flex;align-items:center;justify-content:center}
.feature-ring span{width:58px;height:58px;border-radius:50%;border:2px solid var(--orange);display:flex;align-items:center;justify-content:center}

/* services */
.services-title{left:0;width:1200px;text-align:center;top:2208px;font-size:40px;font-weight:500;color:#222;white-space:nowrap}
.card{position:absolute;top:2331px;height:322px;background:#fff;border-radius:8px;padding:26px 34px}
.card.featured{border:2px solid var(--navy)}
.card h3{margin-top:24px;font-size:22px;font-weight:500;line-height:27px;color:var(--navy)}
.card p{margin-top:22px;font-size:13px;line-height:27px;color:#333;white-space:nowrap}

/* testimonials */
.reviews-title{left:0;width:1200px;text-align:center;top:3012px;font-size:54px;font-weight:400;color:#222}
.slider{left:75px;top:3161px;width:1049px;height:386px;border-radius:14px;overflow:hidden}
.slider-shade{position:absolute;inset:0;background:rgba(10,12,16,.35)}
.quote-mark{position:absolute;left:135px;top:70px;font-size:150px;line-height:150px;color:rgba(255,255,255,.25);font-family:Georgia,serif}
.quote{position:absolute;left:100px;top:95px;width:850px;text-align:center;font-size:15px;line-height:27px;color:#fff;font-weight:500;white-space:nowrap}
.reviewer{position:absolute;left:392px;top:280px;display:flex;align-items:center;gap:16px;color:#fff}
.avatar{width:66px;height:66px;border-radius:50%;background:#b58f78;border:3px solid #fff}
.reviewer b{display:block;font-weight:500;font-size:16px}
.stars{color:#f7c21a;font-size:14px;letter-spacing:1px}
.dots{position:absolute;left:475px;top:340px;display:flex;gap:10px}
.dots i{width:10px;height:10px;border-radius:50%;background:rgba(255,255,255,.45)}
.dots i:first-child{background:#fff}
.arrow{position:absolute;top:3335px;width:34px;height:34px;border-radius:50%;background:#fff;box-shadow:0 2px 8px rgba(0,0,0,.15);display:flex;align-items:center;justify-content:center}

/* contact */
.contact-title{left:72px;top:3795px;font-size:54px;font-weight:400;color:#222}
.contact-rule{left:72px;top:3867px;width:76px;height:4px;background:var(--orange)}
.contact-text{left:78px;top:3928px;width:540px;font-size:13.5px;line-height:22px;color:#333;white-space:nowrap}
.field{position:absolute;background:#fff;border:1px solid var(--line);border-radius:3px;font-size:13px;color:#999;padding:0 20px;display:flex;align-items:center}
.field.area{align-items:flex-start;padding-top:26px}
.submit{left:72px;top:4316px;width:168px;height:50px;border-radius:25px;font-weight:500;font-size:18px}

/* footer */
.footer{left:0;top:4468px;width:1200px;height:507px}
.fcol{position:absolute;color:#fff}
.fcol h4{font-size:16px;font-weight:500;letter-spacing:.3px}
.fcol .mark{position:relative;width:42px;height:2px;background:#fff;margin-top:10px}
.fcol .mark::before{content:"";position:absolute;left:0;top:-3px;width:8px;height:8px;border-radius:50%;background:#fff}
.links{list-style:none;margin-top:38px;font-size:13px}
.links li{height:27px}
.links li::before{content:"»";margin-right:8px}
.info{display:flex;gap:20px;margin-top:22px;font-size:12.5px;line-height:16px;white-space:nowrap}
.info-ico{width:27px;height:27px;border:1px solid #fff;border-radius:4px;display:flex;align-items:center;justify-content:center;flex:none}
.news-text{margin-top:30px;font-size:12.5px;line-height:17px;white-space:nowrap}
.news-field{margin-top:14px;width:208px;height:36px;border:1.5px solid #fff;border-radius:18px;display:flex;align-items:center;justify-content:space-between;padding:0 6px 0 16px;font-size:11px;color:rgba(255,255,255,.7)}
.copyright{left:0;top:4975px;width:1200px;height:54px;background:var(--orange);color:#fff;font-size:11px;display:flex;align-items:center;justify-content:center}
</style>
</head>
<body>

<svg class="abs" style="left:0;top:0" width="1200" height="5029" aria-hidden="true">
  <path d="M0 113H1200V1005Q600 1200 0 1005Z" fill="#f8f7f8"/>
  <path d="M0 1990H1200V2770Q600 2965 0 2770Z" fill="#f8f7f8"/>
  <path d="M0 3697H1200V4975H0Z" fill="#f8f7f8"/>
  <path d="M0 4462Q600 4745 1200 4462V4975H0Z" fill="#2d3a7e"/>
</svg>

<header class="site-header">
  <div class="brand">YOUR HARBOR AGENT</div>
  <nav class="nav">
    <span class="active">HOME</span><span>ABOUT US</span><span>SERVICES</span><span>TESTIMONIALS</span><span>BLOG</span>
  </nav>
  <div class="nav-cta">CONTACT US</div>
</header>

<h1 class="abs hero-title">Our Commitment is that<br>You Find Your Place</h1>
<p class="abs hero-text">Lorem ipsum dolor sit amet consectetur. Accumsan<br>lacus neque nunc convallis eleifend vitae</p>
<div class="btn btn-fill" style="left:75px;top:523px;width:226px;height:70px">View Properties</div>
<div class="btn btn-line" style="left:318px;top:523px;width:226px;height:70px">Contact Us</div>
<div class="photo" role="img" aria-label="Modern multi-storey glass apartment building" style="left:597px;top:197px;width:511px;height:523px;border-radius:256px 256px 0 0;background:linear-gradient(180deg,#dfe4ea 0%,#c6ccd2 40%,#8e969c 75%,#5f666c 100%)"></div>

<div class="abs search-panel">
  <div class="select" style="left:33px">Property type</div>
  <div class="select" style="left:242px">Sell Or Rent</div>
  <div class="select" style="left:451px">Budget</div>
  <div class="select" style="left:661px">Location</div>
  <div class="search-btn">Search
    <svg width="15" height="15" viewBox="0 0 16 16" fill="none" stroke="#fff" stroke-width="1.6"><circle cx="7" cy="7" r="5"/><path d="M11 11l3.5 3.5"/></svg>
  </div>
</div>

<svg class="abs" style="left:39px;top:1184px" width="490" height="502" aria-hidden="true">
  <path d="M50 60C110 -10 200 0 260 40C330 85 460 90 480 200C500 320 420 420 300 470C180 520 70 490 40 400C15 320 -20 140 50 60Z" fill="none" stroke="#ee7a35" stroke-width="2"/>
</svg>
<div class="photo" role="img" aria-label="Hands holding a small model house and keys" style="left:58px;top:1208px;width:455px;height:470px;border-radius:45% 55% 50% 50% / 40% 45% 55% 60%;background:linear-gradient(135deg,#f1f1f1 0%,#e6ddd6 50%,#cdb4a0 100%)"></div>

<div class="tag" style="left:601px;top:1228px">ABOUT US <i></i></div>
<h2 class="abs about-title">Your Harbor Agent</h2>
<p class="abs about-text">Duis pulvinar metus elit, ut aliquam est sollicitudin finibus. Integer lobortis<br>est interdum. Suspendisse nunc est, varius quis fringilla ac, commodo a<br>ante. Praesent non elit cursus, aliquam sapien quis, dictum tortor.Duis<br>pulvinar metus elit, ut aliquam est sollicitudin finibus.</p>

<div class="feature" style="left:601px;top:1466px">
  <div class="feature-ring"><span><svg width="28" height="28" viewBox="0 0 28 28" fill="none" stroke="#ee7a35" stroke-width="1.6"><path d="M3 13L14 4l11 9M6 11v13h16V11M11 24v-7h6v7"/></svg></span></div>
  <div>Smart Home<br>Design</div>
</div>
<div class="feature" style="left:840px;top:1466px">
  <div class="feature-ring"><span><svg width="28" height="28" viewBox="0 0 28 28" fill="none" stroke="#ee7a35" stroke-width="1.6"><path d="M3 20c4-1 7-3 11-1l6-3c2-1 4 1 2 2l-8 5H8"/><circle cx="15" cy="9" r="4"/><path d="M15 3v2M15 13v2M9 9h2M19 9h2"/></svg></span></div>
  <div>Expert<br>guidance</div>
</div>
<div class="feature" style="left:601px;top:1566px">
  <div class="feature-ring"><span><svg width="28" height="28" viewBox="0 0 28 28" fill="none" stroke="#ee7a35" stroke-width="1.6"><circle cx="14" cy="14" r="4"/><path d="M14 3v4M14 21v4M3 14h4M21 14h4M6 6l3 3M19 19l3 3M22 6l-3 3M9 19l-3 3"/></svg></span></div>
  <div>Integrated<br>services</div>
</div>
<div class="feature" style="left:840px;top:1566px">
  <div class="feature-ring"><span><svg width="28" height="28" viewBox="0 0 28 28" fill="none" stroke="#ee7a35" stroke-width="1.6"><circle cx="14" cy="14" r="10"/><path d="M9 14a5 5 0 0110 0v3M8 14v3h2v-3zM18 14v3h2v-3z"/></svg></span></div>
  <div>Dedicated<br>support 24/7</div>
</div>
<div class="btn btn-fill" style="left:599px;top:1697px;width:227px;height:71px">Know More</div>

<div class="tag" style="left:491px;top:2174px"><i></i>SERVICES<i></i></div>
<h2 class="abs services-title">Key features &amp; benefits of Your Harbor Agent</h2>

<div class="card" style="left:78px;width:328px">
  <svg width="74" height="74" viewBox="0 0 74 74" fill="none" stroke="#ee7a35" stroke-width="2"><path d="M6 36L37 8l31 28M14 30v22M60 30v28H34"/><circle cx="30" cy="30" r="4"/><circle cx="44" cy="44" r="4"/><path d="M46 26L28 48"/><path d="M4 56h12l8 4h10M4 68h8l10 2h14l16-10"/></svg>
  <h3>Mortgage House<br>Services</h3>
  <p>Lorem ipsum dolor sit amet conse ct<br>&nbsp;Convallis nisl eu consequat nisi in<br>montes odio amet massa.</p>
</div>
<div class="card featured" style="left:435px;width:330px">
  <svg width="74" height="74" viewBox="0 0 74 74" fill="none" stroke="#ee7a35" stroke-width="2"><path d="M6 34L36 8l30 26M12 30v36h50V30M22 40h10v10H22zM42 40h10v10H42z"/><rect x="30" y="52" width="38" height="16" rx="3" fill="#fff"/><text x="49" y="64" font-size="11" font-family="Poppins,sans-serif" fill="#ee7a35" stroke="none" text-anchor="middle" font-weight="600">RENT</text></svg>
  <h3>Rent House<br>Services</h3>
  <p>Lorem ipsum dolor sit amet conse cte<br>tur. Convallis nisl eu consequat nisi in<br>montes odio amet massa.</p>
</div>
<div class="card" style="left:796px;width:328px">
  <svg width="74" height="74" viewBox="0 0 74 74" fill="none" stroke="#ee7a35" stroke-width="2"><path d="M8 38L38 14l30 24M16 32v34h44V32M30 66V48h16v18M10 8h20v8H10zM20 16v10"/><path d="M6 66h64"/></svg>
  <h3>Build House<br>Services</h3>
  <p>Lorem ipsum dolor sit amet consect<br>etur. Convallis nisl eu consequat nisi in<br>montes odio amet massa.</p>
</div>
<div class="btn btn-fill" style="left:486px;top:2718px;width:226px;height:70px">View All Services</div>

<div class="tag" style="left:464px;top:2979px"><i></i>TESTIMONIALS<i></i></div>
<h2 class="abs reviews-title">Client Reviews</h2>

<div class="abs slider">
  <div class="photo" role="img" aria-label="Modern villa with pool at dusk" style="inset:0;background:linear-gradient(180deg,#7a7c80 0%,#4a4d52 45%,#2a2d31 70%,#2e4852 100%)"></div>
  <div class="slider-shade"></div>
  <div class="quote-mark">“</div>
  <p class="quote">Lorem ipsum dolor sit amet, consectetur adipiscing elit, sed do eiu smod tempor incididunt ut<br>labore et dolore magna aliqua. Quis ipsum suspendisse ultrices gravida. Risus commodo<br>viverra maecenas accumsan lacus vel facilisis.</p>
  <div class="reviewer">
    <div class="avatar" role="img" aria-label="Client portrait"></div>
    <div><b>Marcus Ellery</b><span class="stars">★★★★★</span></div>
  </div>
  <div class="dots"><i></i><i></i><i></i></div>
</div>
<div class="arrow" style="left:30px"><svg width="10" height="10" viewBox="0 0 10 10" fill="none" stroke="#222" stroke-width="1.8"><path d="M6.5 2L3.5 5l3 3"/></svg></div>
<div class="arrow" style="left:1138px"><svg width="10" height="10" viewBox="0 0 10 10" fill="none" stroke="#222" stroke-width="1.8"><path d="M3.5 2l3 3-3 3"/></svg></div>

<h2 class="abs contact-title">Contact Us</h2>
<div class="abs contact-rule"></div>
<p class="abs contact-text">Lorem ipsum dolor sit amet, consectetur adipiscing elit, sed do eiusmod<br>tempor incididunt ut labore et dolore magna aliqua.</p>
<div class="field" style="left:72px;top:4005px;width:223px;height:47px">First Name</div>
<div class="field" style="left:314px;top:4005px;width:224px;height:47px">Last Name</div>
<div class="field" style="left:72px;top:4070px;width:223px;height:47px">Phone</div>
<div class="field" style="left:314px;top:4070px;width:224px;height:47px">Email</div>
<div class="field area" style="left:72px;top:4138px;width:466px;height:142px">Message:</div>
<div class="btn btn-fill submit">Submit</div>
<div class="photo" role="img" aria-label="Model house on architectural plans with drafting tools" style="left:675px;top:3828px;width:429px;height:484px;border-radius:215px 215px 0 0;background:linear-gradient(160deg,#eef1f3 0%,#c9d2d8 45%,#8fa58a 70%,#b9bcc0 100%)"></div>

<footer class="abs footer">
  <div class="fcol" style="left:187px;top:240px">
    <h4>QUICK LINKS</h4><div class="mark"></div>
    <ul class="links"><li>About Us</li><li>Services</li><li>Testimonials</li><li>Blog</li><li>Contact Us</li></ul>
  </div>
  <div class="fcol" style="left:490px;top:240px">
    <h4>CONTACT US</h4><div class="mark"></div>
    <div class="info" style="margin-top:32px"><span class="info-ico"><svg width="13" height="13" viewBox="0 0 14 14" fill="none" stroke="#fff" stroke-width="1.3"><path d="M3 1.5l2 .5 1 3-1.5 1a7 7 0 003 3l1-1.5 3 1 .5 2c-6 2-11-3-9-9z"/></svg></span><div>CALL US<br>8012 555 0147</div></div>
    <div class="info" style="margin-top:16px"><span class="info-ico"><svg width="13" height="13" viewBox="0 0 14 14" fill="none" stroke="#fff" stroke-width="1.3"><rect x="1.5" y="3" width="11" height="8"/><path d="M1.5 3l5.5 4.5L12.5 3"/></svg></span><div>EMAIL US<br>info@harboragent.com</div></div>
    <div class="info" style="margin-top:16px"><span class="info-ico"><svg width="13" height="13" viewBox="0 0 14 14" fill="none" stroke="#fff" stroke-width="1.3"><path d="M7 13s-4.5-4.5-4.5-7.5a4.5 4.5 0 019 0C11.5 8.5 7 13 7 13z"/><circle cx="7" cy="5.5" r="1.6"/></svg></span><div>Address line Dummy Here<br>Address line Here</div></div>
  </div>
  <div class="fcol" style="left:886px;top:240px">
    <h4>OUR NEWSLETTER</h4><div class="mark"></div>
    <p class="news-text">Subscribe our newsletter to get<br>the latest news.</p>
    <div class="news-field">Enter Email Address
      <svg width="24" height="24" viewBox="0 0 24 24" fill="none" stroke="#fff" stroke-width="1.4"><circle cx="12" cy="12" r="10"/><path d="M7 12h10M13 8l4 4-4 4"/></svg>
    </div>
  </div>
</footer>
<div class="abs copyright">Copyright © 2024 All Rights Reserved By Company name</div>

</body>
</html>
```